Business card design for IT consulting company

Looking for a simple, modern, clean business card design.
Open to reworking our existing logo.

Attached is our current business cards which we do not like.
Ideally double sided with something simple on the back.
Rectangle / Horizonal only.
No rounded edges on the card.
White as the dominate color is preferred.

Target Market(s)

clients, legal, oil & gas, medical, professionals

Industry/Entity Type

IT, tech, consulting

Contact Information for Business Card

Name, Title, email, phone, cell, website

Font styles to use
Sans Serif

Requirements
Must have
• Clean design
Should not have
• loud colors or unusual fonts, etc

```html
<!DOCTYPE html>
<html lang="en">
<head>
<meta charset="utf-8">
<title>Kovra Solutions – Business Card</title>
<link rel="stylesheet" href="https://fonts.googleapis.com/css2?family=Archivo:wght@700&family=Montserrat:wght@400;700&display=swap">
<style>
  :root {
    --page-bg: #ededed;
    --card-bg: #ffffff;
    --ink: #0d0d0d;
    --navy: #262770;
    --yellow: #f9c62f;
    --red: #ee4055;
    --sky: #45aee3;
    --text-dark: #1a1a1a;
    --white: #ffffff;
  }
  * { margin: 0; padding: 0; box-sizing: border-box; }
  html, body {
    width: 1200px;
    height: 1200px;
    overflow: hidden;
    background: var(--page-bg);
  }
  .card {
    position: absolute;
    left: 162.5px;
    width: 875px;
    height: 525px;
    background: var(--card-bg);
  }
  .card--front { top: 62.5px; }
  .card--back { top: 617.5px; }

  /* Front */
  .brand-lockup {
    position: absolute;
    left: 0; right: 0;
    top: 196px;
    display: flex;
    align-items: center;
    justify-content: center;
    gap: 28px;
  }
  .brand-square {
    width: 128px;
    height: 128px;
    background: var(--navy);
    border-radius: 12px;
  }
  .brand-name {
    font-family: "Archivo", "Helvetica Neue", Arial, sans-serif;
    font-weight: 700;
    font-size: 66px;
    letter-spacing: -0.5px;
    color: var(--ink);
  }

  /* Back */
  .back-brand {
    position: absolute;
    left: 107px;
    top: 76px;
    display: flex;
    align-items: center;
    gap: 18px;
  }
  .back-brand .brand-square {
    width: 146px;
    height: 146px;
    border-radius: 12px;
  }
  .back-brand .brand-name {
    font-size: 34px;
    letter-spacing: 0;
  }

  .name-tag {
    position: absolute;
    left: 524.5px;
    top: 179.5px;
    width: 350.5px;
    height: 143px;
  }
  .name-tag__accent {
    position: absolute;
    left: 0; top: 0;
    width: 8px;
    height: 143px;
    background: var(--yellow);
  }
  .name-tag__band {
    position: absolute;
    left: 8px;
    top: 15px;
    right: 0;
    height: 116px;
    background: var(--navy);
    color: var(--white);
    font-family: "Montserrat", Arial, sans-serif;
  }
  .person-name {
    position: absolute;
    left: 37px;
    top: 20px;
    font-weight: 700;
    font-size: 39px;
    line-height: 1;
  }
  .person-title {
    position: absolute;
    left: 61px;
    top: 67px;
    font-weight: 400;
    font-size: 24px;
    line-height: 1;
  }

  .contact-list {
    position: absolute;
    left: 106px;
    top: 290px;
    list-style: none;
    font-family: "Montserrat", Arial, sans-serif;
    font-size: 20px;
    color: var(--text-dark);
  }
  .contact-item {
    display: flex;
    align-items: center;
    height: 40px;
    margin-bottom: 1px;
  }
  .contact-icon {
    width: 26px;
    height: 26px;
    margin-right: 29px;
    flex: none;
  }
</style>
</head>
<body>

<section class="card card--front" aria-label="Card front">
  <div class="brand-lockup">
    <div class="brand-square" aria-hidden="true"></div>
    <span class="brand-name">Kovra Solutions</span>
  </div>
</section>

<section class="card card--back" aria-label="Card back">
  <div class="back-brand">
    <div class="brand-square" aria-hidden="true"></div>
  </div>

  <div class="name-tag">
    <div class="name-tag__accent"></div>
    <div class="name-tag__band">
      <span class="person-name">Daniel Reyes</span>
      <span class="person-title">IT Consultant</span>
    </div>
  </div>

  <ul class="contact-list">
    <li class="contact-item">
      <svg class="contact-icon" viewBox="0 0 24 24" aria-hidden="true">
        <rect x="2" y="5" width="20" height="14" fill="var(--red)"/>
        <path d="M2.5 5.5 L12 13 L21.5 5.5" fill="none" stroke="#fff" stroke-width="1.6"/>
        <path d="M2.5 18.5 L9.5 11.5 M21.5 18.5 L14.5 11.5" fill="none" stroke="#fff" stroke-width="1.2"/>
      </svg>
      <span>daniel.reyes@kovra.ca</span>
    </li>
    <li class="contact-item">
      <svg class="contact-icon" viewBox="0 0 24 24" aria-hidden="true">
        <path fill="var(--red)" d="M6.6 10.8c1.4 2.8 3.8 5.1 6.6 6.6l2.2-2.2c.3-.3.7-.4 1-.2 1.1.4 2.3.6 3.6.6.6 0 1 .4 1 1V20c0 .6-.4 1-1 1C10.6 21 3 13.4 3 4c0-.6.4-1 1-1h3.5c.6 0 1 .4 1 1 0 1.3.2 2.5.6 3.6.1.3 0 .7-.2 1l-2.3 2.2z"/>
      </svg>
      <span>(888) 555-0142</span>
    </li>
    <li class="contact-item">
      <svg class="contact-icon" viewBox="0 0 24 24" aria-hidden="true">
        <rect x="6.5" y="1.5" width="11" height="21" rx="2" fill="none" stroke="var(--red)" stroke-width="1.8"/>
        <line x1="6.5" y1="18" x2="17.5" y2="18" stroke="var(--red)" stroke-width="1.5"/>
        <circle cx="12" cy="20.2" r="0.9" fill="var(--red)"/>
      </svg>
      <span>(604) 555-0187</span>
    </li>
    <li class="contact-item">
      <svg class="contact-icon" viewBox="0 0 24 24" aria-hidden="true">
        <g fill="none" stroke="var(--red)" stroke-width="1.6">
          <circle cx="12" cy="12" r="9.5"/>
          <ellipse cx="12" cy="12" rx="4.2" ry="9.5"/>
          <line x1="2.5" y1="12" x2="21.5" y2="12"/>
          <path d="M4 7h16M4 17h16"/>
        </g>
      </svg>
      <span>www.kovra.ca</span>
    </li>
  </ul>
</section>

</body>
</html>
```